Website to showcase Pram Trail Races that will be held in Woodland Trust Board areas in the UK

Looking for a website, designed in WordPress, to provide information on family orientated running events that I'm organising in the UK (I've registered the website address pramtrailraces.co.uk). Refer to the Project Brief document however as a summary:
These events are unique, as they are for people running with a child in a buggy (or in a wheelchair) and will be on carefully designed, traffic-free courses in Woodland Trust Board areas. The events, by using a specialist timing system, will allow runners to start within a two hour window therefore removing the anxiety / rush to get to the start line for the mass start. All events will be centred around a family day with face painting, adventure playgrounds, café and ample parking. Current thinking is a home page that will contain links to four separate pages, information about me and a blog from my Chatterly and Quibbler feeds, one page for two running events being held at Fern Cottage, Marlow Woods (www.woodlandboard.example/ferncottage) in October and December and another page for an event at Rowan Dell Woods (www.woodlandboard.example/rowandell) in November. The third page will be information on the different running buggies available and how people can come and view them at each event and try them out on the course and if they like it they can purchase that buggy for a 10% discount of the RRP. They will need to email me to reserve a buggy for use at the event. The forth page will be information on myself ('About Me' and the details from my other website can be used at this stage). There will be a link from each event page to allow people to enter that particular race online from an external website (links to follow). My current website is an online shop selling running buggies (www.pramtrail.co.uk).

I'm also looking for the website to be published (access to cPanel will be given to allow this).

Attached is my current logo (this will be replaced by a new one currently being designed but is nearly identical) so will be replaced before the website goes live. Also attached are a couple of photos to give an idea on running with a buggy and the different types of areas being used. One of the pictures is the lineup of running buggies so could be used on the third page as it was taken at one of the event forests. Also attached are two logos for the Woodland Trust Board that should be on the home page.

Alongside the website I'm also looking for two flyers to be designed to showcase each running event (to be used on Social Media and public locations such as cafes, nurseries, running clubs, gyms). One flyer for Fern Cottage Marlow Woods event on the 1st October 2017 and the second flyer for the Rowan Dell Woods event on the 5th November 2017. Both these flyers will be a separate project and therefore attract additional payment for each. Will look to offer this work to the winning designer.

Target Market(s)

Families

Industry/Entity Type

Events

Number of Pages Required

5+ page

Font styles to use
Sans Serif

Colors

Designer to choose colors to be used in the design.

Requirements
Must have
• Clear and precise information that each buggy running event is family orientated, on an off-road course that has been carefully planned to be used by a buggy. Different page to highlight the event (i've taken a video of each course so people can see what the terrain is like), course map, course distance, hill profile, timings for the day, travel directions, course dates in 2017 and 2018.
• I'm also looking for the website to be published (access to cPanel will be given to allow this).
• Countdown timer to the next event.
Nice to have
• Map of the UK with the locations highlighted (with a link to the event page). More locations to follow during the rest of 2017.
Should not have
• A lot of writing in small font

```html
<!DOCTYPE html>
<html lang="en">
<head>
<meta charset="utf-8">
<title>Pram Trail Races</title>
<link href="https://fonts.googleapis.com/css2?family=Open+Sans:wght@400;600;700&display=swap" rel="stylesheet">
<style>
  :root {
    --orange: #f7941d;
    --orange-dark: #e07f0a;
    --ink: #333;
    --muted: #7a7a7a;
    --line: #e2e2e2;
    --panel: #f1f1f1;
    --slate: #3e5588;
    --teal: #2fa6d6;
    --footer: #2f2f2f;
    --white: #fff;
  }
  * { box-sizing: border-box; margin: 0; padding: 0; }
  html, body { width: 675px; height: 1200px; overflow: hidden; }
  body { font-family: "Open Sans", sans-serif; color: var(--ink); background: var(--white); position: relative; }

  .site-header { height: 50px; display: flex; align-items: center; justify-content: space-between; padding: 0 22px; border-bottom: 1px solid var(--line); position: relative; }
  .brand { display: flex; align-items: center; gap: 6px; font-weight: 700; font-size: 17px; color: var(--orange); }
  .brand-dot { width: 16px; height: 16px; border-radius: 50%; background: var(--orange); }
  .call-pill { position: absolute; top: 4px; right: 22px; background: var(--orange); color: var(--white); font-size: 6.5px; font-weight: 700; padding: 3px 9px; border-radius: 8px; display: flex; align-items: center; gap: 4px; }
  .main-nav { display: flex; gap: 14px; font-size: 6.5px; font-weight: 700; margin-top: 14px; align-items: center; }
  .main-nav a { color: var(--ink); text-decoration: none; }
  .main-nav a.active { color: var(--orange); }

  .hero { height: 300px; position: relative; background: linear-gradient(180deg, #9fb7a8 0%, #6e8c63 45%, #4f7a34 70%, #3f6b2a 100%); }
  .hero-text { position: absolute; left: 36px; top: 170px; width: 250px; color: var(--white); }
  .hero-text h1 { font-size: 22px; font-weight: 600; margin-bottom: 8px; }
  .hero-text p { font-size: 8.5px; line-height: 1.5; }

  .about { display: flex; padding: 28px 40px 0 36px; gap: 40px; height: 255px; }
  .about-copy { flex: 1; }
  .section-title { color: var(--orange); font-size: 17px; font-weight: 600; margin-bottom: 14px; }
  .about-copy p { font-size: 7px; line-height: 1.7; color: var(--muted); margin-bottom: 10px; }
  .btn { display: inline-block; background: var(--orange); color: var(--white); font-size: 8px; font-weight: 600; padding: 7px 14px; border-radius: 2px; margin-top: 8px; }
  .about-photo { width: 165px; height: 165px; border-radius: 50%; border: 5px solid #ddd; background: radial-gradient(circle at 50% 40%, #c9b9a8 0%, #8a9a6a 60%, #5d7a45 100%); margin-top: 6px; }

  .social { background: var(--panel); height: 265px; padding: 25px 50px; display: flex; gap: 20px; }
  .feed { flex: 1; background: var(--white); border: 1px solid var(--line); }
  .feed-head { height: 24px; display: flex; align-items: center; padding: 0 10px; color: var(--white); font-weight: 700; font-size: 12px; }
  .feed-head.chatterly { background: var(--slate); }
  .feed-head.quibbler { background: var(--teal); }
  .post { display: flex; gap: 8px; padding: 10px; border-bottom: 1px solid var(--line); }
  .avatar { width: 22px; height: 22px; background: #c8c8c8; flex: none; }
  .post-name { font-size: 6.5px; font-weight: 700; color: var(--ink); }
  .post-body { font-size: 6px; color: var(--muted); line-height: 1.5; margin: 2px 0 5px; }
  .post-actions { display: flex; gap: 10px; font-size: 5.5px; color: var(--muted); }
  .comment-box { margin: 12px 10px; border: 1px solid var(--line); height: 16px; font-size: 5.5px; color: #aaa; padding: 4px 6px; }

  .location { text-align: center; padding-top: 24px; height: 295px; }
  .location .section-title { margin-bottom: 4px; }
  .location-sub { font-size: 6.5px; color: var(--muted); margin-bottom: 12px; }
  .map { width: 540px; height: 198px; margin: 0 auto; background: linear-gradient(135deg, #efe6d3 0%, #e3e8cf 40%, #cfe0b8 70%, #eee3cc 100%); border: 1px solid var(--line); }

  .site-footer { position: absolute; left: 0; bottom: 0; width: 675px; height: 34px; background: var(--footer); display: flex; align-items: center; justify-content: space-between; padding: 0 22px; color: #bbb; font-size: 6px; }
  .footer-social { display: flex; gap: 5px; }
  .footer-social span { width: 14px; height: 14px; border-radius: 50%; border: 1px solid #888; }
</style>
</head>
<body>
  <header class="site-header">
    <div class="brand"><span class="brand-dot"></span>pramtrailraces</div>
    <div class="call-pill">
      <svg width="7" height="7" viewBox="0 0 24 24"><path fill="#fff" d="M6.6 10.8a15 15 0 006.6 6.6l2.2-2.2c.3-.3.7-.4 1-.2 1.1.4 2.3.6 3.6.6.6 0 1 .4 1 1V20c0 .6-.4 1-1 1A17 17 0 013 4c0-.6.4-1 1-1h3.5c.6 0 1 .4 1 1 0 1.3.2 2.5.6 3.6.1.3 0 .7-.2 1z"/></svg>
      CALL US: (0800) 555 0142
    </div>
    <nav class="main-nav">
      <a class="active" href="#">HOME</a>
      <a href="#">FERN COTTAGE RUNNING EVENT</a>
      <a href="#">ROWAN DELL RUNNING EVENT</a>
      <a href="#">OUR INFORMATION</a>
      <a href="#">ABOUT US</a>
      <svg width="8" height="8" viewBox="0 0 24 24"><circle cx="10" cy="10" r="7" fill="none" stroke="#333" stroke-width="3"/><path d="M15 15l6 6" stroke="#333" stroke-width="3"/></svg>
    </nav>
  </header>

  <section class="hero" role="img" aria-label="Photo of a child in a running buggy on a grassy park with runners and a dog">
    <div class="hero-text">
      <h1>Pram Trail Races</h1>
      <p>Pram Trail Races is a brand new concept developed by Dan Hollis, a competitive runner &amp; father of a toddler daughter.</p>
    </div>
  </section>

  <section class="about">
    <div class="about-copy">
      <h2 class="section-title">About Us Our Company</h2>
      <p>The running events are aimed at getting kids to experience the outdoors while parents run along the trails. Courses are carefully planned, traffic-free and safe for every type of buggy, with a flexible two hour start window so nobody has to rush to the line.</p>
      <p>The events are unique, as they are for people running with a child in a buggy or wheelchair and are on carefully designed, off-road courses. Each event is a family day out with face painting, playgrounds and a café.</p>
      <a class="btn">Read More</a>
    </div>
    <div class="about-photo" role="img" aria-label="Round photo of the organiser with family and dog in a park"></div>
  </section>

  <section class="social">
    <div class="feed">
      <div class="feed-head chatterly">Chatterly</div>
      <div class="post"><div class="avatar"></div><div><div class="post-name">Admin</div><div class="post-body">Great morning on the trails today, thanks to every family who came along to run with us!</div><div class="post-actions"><span>Like</span><span>Comment</span><span>Share</span></div></div></div>
      <div class="post"><div class="avatar"></div><div><div class="post-name">Admin</div><div class="post-body">Great morning on the trails today, thanks to every family who came along to run with us!</div><div class="post-actions"><span>Like</span><span>Comment</span><span>Share</span></div></div></div>
      <div class="comment-box">Write a comment...</div>
    </div>
    <div class="feed">
      <div class="feed-head quibbler">Quibbler</div>
      <div class="post"><div class="avatar"></div><div><div class="post-name">Admin</div><div class="post-body">Great morning on the trails today, thanks to every family who came along to run with us!</div><div class="post-actions"><span>Like</span><span>Comment</span><span>Share</span></div></div></div>
      <div class="post"><div class="avatar"></div><div><div class="post-name">Admin</div><div class="post-body">Great morning on the trails today, thanks to every family who came along to run with us!</div><div class="post-actions"><span>Like</span><span>Comment</span><span>Share</span></div></div></div>
      <div class="comment-box">Write a comment...</div>
    </div>
  </section>

  <section class="location">
    <h2 class="section-title">Event Location</h2>
    <p class="location-sub">Pram Trail Races is a brand new concept developed by Dan Hollis, a competitive runner and father of a toddler daughter.</p>
    <div class="map" role="img" aria-label="Street map showing the event location"></div>
  </section>

  <footer class="site-footer">
    <span>© Copyright 2017 Pram Trail Races All Rights Reserved</span>
    <div class="footer-social"><span></span><span></span><span></span><span></span><span></span></div>
  </footer>
</body>
</html>
```